Quote Cards for Social Media RV

I would like to put these quotes over one of the pictures attached; One Quote per picture, and I want the quote to be bold or easy to read as well. I provided a few reference graphics that I really like as examples below. In very small letters at the bottom add @RVCarloweDaily

All of the pictures are attached; you can pick any photo and add one quote to it; but no stock photography

Target Market(s)

women trying to lose weight

Requirements
Must have
• quotes and pictures attached
Should not have
• no stock photography

```html
<!DOCTYPE html>
<html lang="en">
<head>
<meta charset="utf-8">
<title>Quote Card – Natural Solution</title>
<link rel="stylesheet" href="https://fonts.googleapis.com/css2?family=Comfortaa:wght@500;600&display=swap">
<style>
  :root {
    --card-bg: #ffcce5;
    --photo-light: #ffd6ea;
    --photo-mid: #f9bfdb;
    --photo-deep: #f2aed0;
    --scrim: rgba(255, 214, 234, 0.55);
    --ink-pink: #ff0a99;
  }
  * { margin: 0; padding: 0; box-sizing: border-box; }
  html, body {
    width: 1200px;
    height: 1200px;
    overflow: hidden;
    background: var(--card-bg);
  }
  .quote-card {
    position: relative;
    width: 1200px;
    height: 1200px;
    overflow: hidden;
    font-family: "Comfortaa", sans-serif;
    color: var(--ink-pink);
  }
  .quote-card__photo {
    position: absolute;
    inset: 0;
    background:
      radial-gradient(ellipse 70% 60% at 75% 30%, var(--photo-light) 0%, transparent 70%),
      radial-gradient(ellipse 60% 55% at 20% 85%, var(--photo-deep) 0%, transparent 70%),
      linear-gradient(160deg, var(--photo-light) 0%, var(--photo-mid) 55%, var(--photo-deep) 100%);
  }
  .quote-card__scrim {
    position: absolute;
    inset: 0;
    background: var(--scrim);
  }
  .quote-card__text {
    position: absolute;
    left: 108px;
    top: 276px;
    font-size: 86px;
    font-weight: 600;
    line-height: 119px;
    letter-spacing: -2px;
    white-space: nowrap;
  }
  .quote-card__line { display: block; }
  .quote-card__handle {
    position: absolute;
    right: 74px;
    bottom: 54px;
    font-size: 25px;
    font-weight: 600;
    letter-spacing: -0.3px;
  }
</style>
</head>
<body>
  <main class="quote-card">
    <div class="quote-card__photo" role="img" aria-label="Client-supplied lifestyle photo in soft pink tones behind the quote"></div>
    <div class="quote-card__scrim"></div>
    <p class="quote-card__text">
      <span class="quote-card__line">Struggling with</span>
      <span class="quote-card__line">bloating and belly fat?</span>
      <span class="quote-card__line">Try this natural solution</span>
      <span class="quote-card__line">tonight, and wake up</span>
      <span class="quote-card__line">feeling lighter!</span>
    </p>
    <p class="quote-card__handle">@RVCarloweDaily</p>
  </main>
</body>
</html>
```